KLV Reply Yield Digest Cover

The Outreach Commerce Guild (KLV) is releasing its Reply Yield Digest for 2015. The Reply Yield survey provides success metrics for the direct marketing community. The survey breaks down findings where possible into several segments so that marketers see clearly how organizations like them are performing in their campaigns.

The purpose of this creative is to serve as the cover of the book. This cover image will be the books “face” to the industry and be used on the website, in e-commerce and general promotions.

The cover should look nothing like the 2012 cover, attached. We would like the cover to express the anticipation of the data inside which is the latest metrics for how direct mail, email, paid search, online display, advertising, and telephone marketing perform as marketing channels curated from around the industry.

PLEASE SEE THE ATTACHED BRIEF FOR MORE INFORMATION.

Target Market(s)

See attached creative brief.

Industry/Entity Type

E-Commerce

Font styles to use
Serif
Sans Serif

Requirements
Must have
• See attached creative brief.
Nice to have

```html
<!DOCTYPE html>
<html lang="en">
<head>
<meta charset="utf-8">
<title>KLV Reply Yield Digest 2015 Cover</title>
<link rel="stylesheet" href="https://fonts.googleapis.com/css2?family=EB+Garamond:wght@400&display=swap">
<style>
  :root {
    --backdrop: #e9e6e2;
    --paper: #ffffff;
    --ink-blue: #1f5aa6;
    --rule-blue: #5a86c2;
    --cube-blue: #1e5fa8;
    --cube-green: #76b843;
    --cube-pale: #c9e0a8;
    --cube-grey: #e4e6e8;
    --cube-yellow: #f2c21b;
  }
  * { box-sizing: border-box; margin: 0; padding: 0; }
  html, body {
    width: 1200px;
    height: 900px;
    overflow: hidden;
    background: var(--backdrop);
  }
  .canvas {
    position: relative;
    width: 1200px;
    height: 900px;
  }
  .cover {
    position: absolute;
    left: 275px;
    top: 30px;
    width: 650px;
    height: 840px;
    background: var(--paper);
    box-shadow: 0 2px 14px rgba(0, 0, 0, 0.12);
    font-family: "EB Garamond", Georgia, serif;
    color: var(--ink-blue);
  }
  .cube-artwork {
    position: absolute;
    z-index: 1;
    left: 40px;
    top: 60px;
    width: 540px;
    height: 530px;
    background:
      radial-gradient(circle at 50% 52%, var(--cube-blue) 0 16%, transparent 17%),
      radial-gradient(circle at 28% 30%, var(--cube-green) 0 12%, transparent 13%),
      radial-gradient(circle at 72% 42%, var(--cube-green) 0 11%, transparent 12%),
      radial-gradient(circle at 40% 18%, var(--cube-blue) 0 9%, transparent 10%),
      radial-gradient(circle at 60% 78%, var(--cube-pale) 0 11%, transparent 12%),
      radial-gradient(circle at 22% 70%, var(--cube-grey) 0 13%, transparent 14%),
      radial-gradient(circle at 30% 52%, var(--cube-yellow) 0 5%, transparent 6%),
      radial-gradient(ellipse at 50% 50%, #eef3e6 0%, rgba(255, 255, 255, 0) 70%);
    border-radius: 8px;
  }
  .cover-title {
    position: absolute;
    z-index: 2;
    left: 362px;
    top: 80px;
    font-weight: 400;
    font-size: 34px;
    line-height: 1.05;
    letter-spacing: 0.5px;
    white-space: nowrap;
  }
  .title-rule {
    position: absolute;
    z-index: 2;
    left: 340px;
    top: 158px;
    width: 270px;
    height: 20px;
  }
  .tagline {
    position: absolute;
    z-index: 2;
    left: 72px;
    top: 672px;
    font-size: 19px;
    letter-spacing: 1.2px;
    font-weight: 400;
  }
  .publisher-mark {
    position: absolute;
    z-index: 2;
    left: 72px;
    top: 702px;
    display: flex;
    align-items: center;
    gap: 12px;
  }
  .publisher-square {
    width: 22px;
    height: 22px;
    background: var(--cube-green);
  }
  .publisher-name {
    font-size: 52px;
    line-height: 1;
    font-weight: 400;
    color: var(--ink-blue);
  }
</style>
</head>
<body>
  <main class="canvas">
    <section class="cover">
      <div class="cube-artwork" role="img" aria-label="Cluster of floating 3D cubes in blue, green, pale green, yellow and grey, bearing icons for search, ideas, folders, growth chart, power, refresh and forward arrows"></div>
      <h1 class="cover-title">Reply Yield<br>Digest for 2015</h1>
      <svg class="title-rule" viewBox="0 0 270 20" aria-hidden="true">
        <path d="M2 17 Q135 2 268 4" fill="none" stroke="var(--rule-blue)" stroke-width="1.4"/>
      </svg>
      <p class="tagline">Data to Benchmark All of Your Marketing Campaigns</p>
      <div class="publisher-mark">
        <span class="publisher-square" aria-hidden="true"></span>
        <span class="publisher-name">KLV</span>
      </div>
    </section>
  </main>
</body>
</html>
```